Performance Psychology Business Card Design + Letterhead

I require a new business card and letterhead for my consulting business. I am a psychologist working predominantly in sport psychology and organisational psychology. I consult to elite athletes and corporates.
I provide counselling services, workshops, assessments, and group sessions.
I'd like to use the colours in the logo.
My current card and letterhead is predominantly white - which I do like, but I'm up to try something different as well!
The letterhead doesn't need to have my name or title on it - but it can
The company is about success, achievement and reaching potential.
My website is at www.harvodel.com.au
I have changed some of my contact details, so I definitely need a new card and I would like this project to go ahead.
Thank you for putting the time into my design - I'm really excited about a new card and appreciate your contribution.
*IMPORTANT: The Fax Number Should be: 07 41 58 39 06
Target Market(s)
Elite athletes and teams
Corporate clients
Industry/Entity Type
Business
Contact Information for Business Card
Dr Marlise Quenby
Director (this is optional - I don't have to have this on there)
Level 2, 48 Wexbridge St
Carranby Qld 4852
M: 0431 562 047
F: 07 41 306 259
E: mq@harvodel.com.au
W: www.harvodel.com.au
Requirements
Must have
- Logo - I have one with a white background and one with blue - don't mind which one is used. Currently I have the white logo on letterhead and cards.
I would like to have the catchphrase of the company
... Rise To Your Finest
on the card somewhere.
Nice to have
- On my current card I have a few lines on the back to write appointment times for clients - however this isn't essential
I also have some of the key services provided:
- Performance Enhancement
- Assessment & Reports
- Individual & Group Counselling
- Executive coaching & Motivation
- Seminars & Workshops
I have a QR file - don't have it on my current card, but thinking it could go on the business card (probably not letterhead?). For some reason I can only load one file, so can send it through if it's needed.

```html
<!DOCTYPE html>
<html lang="en">
<head>
<meta charset="utf-8">
<title>Harvodel Psychology – Business Card</title>
<link rel="stylesheet" href="https://fonts.googleapis.com/css2?family=Questrial&family=Arimo:wght@400;700&display=swap">
<style>
  :root {
    --navy: #0e0f6b;
    --sky: #1aa3e0;
    --ink: #1c1d70;
    --paper: #ffffff;
    --backdrop: #e9eaee;
    --rule: #2a2b7a;
  }
  * { box-sizing: border-box; margin: 0; padding: 0; }
  html, body { width: 1200px; height: 934px; overflow: hidden; }
  body {
    background: var(--backdrop);
    position: relative;
    font-family: "Questrial", sans-serif;
    color: var(--ink);
  }
  .card {
    position: absolute;
    width: 540px;
    height: 330px;
    background: var(--paper);
    box-shadow: 0 10px 28px rgba(0,0,0,0.12);
    overflow: hidden;
  }

  /* Back of card */
  .card-back { left: 70px; top: 130px; display: flex; }
  .appointments { width: 50%; padding: 38px 20px 0 30px; }
  .appointments h2 {
    font-weight: 400; font-size: 15px; letter-spacing: 0.5px;
    text-align: center; color: var(--ink); margin-bottom: 20px;
  }
  .appointment-list { list-style: none; }
  .appointment-list li {
    font-family: "Arimo", sans-serif; font-size: 12.5px;
    display: flex; align-items: flex-end; gap: 4px; margin-bottom: 17px;
    white-space: nowrap;
  }
  .slot { display: inline-block; border-bottom: 1px solid var(--rule); height: 12px; }
  .slot.time { width: 22px; }
  .slot.place { width: 92px; margin-left: 6px; }
  .slot.date { width: 16px; }
  .services-panel {
    width: 50%; background: var(--navy); color: #fff;
    padding: 44px 20px 0 34px;
  }
  .brand { display: flex; align-items: center; gap: 10px; }
  .brand-dot { width: 16px; height: 16px; border-radius: 50%; background: var(--sky); }
  .brand-name {
    font-family: "Arimo", sans-serif; font-weight: 700; font-size: 30px;
  }
  .services-panel .brand-name { color: #fff; }
  .brand-sub {
    font-size: 11px; letter-spacing: 5px; text-transform: uppercase;
    margin: 4px 0 24px 26px;
  }
  .service-list { list-style: none; font-family: "Arimo", sans-serif; font-size: 12.5px; }
  .service-list li { margin-bottom: 5px; padding-left: 16px; position: relative; white-space: nowrap; }
  .service-list li::before {
    content: ""; position: absolute; left: 2px; top: 6px;
    width: 5px; height: 5px; border-radius: 50%; background: #fff;
  }

  /* Front of card */
  .card-front { left: 590px; top: 474px; }
  .front-brand { position: absolute; left: 36px; top: 88px; }
  .front-brand .brand-name { color: var(--navy); font-size: 40px; }
  .front-brand .brand-dot { width: 20px; height: 20px; }
  .front-brand .brand-sub { color: var(--navy); font-size: 12px; letter-spacing: 6px; margin-left: 32px; }
  .tagline {
    position: absolute; left: 36px; top: 226px;
    font-size: 22px; color: var(--sky);
  }
  .website {
    position: absolute; left: 70px; top: 258px;
    font-family: "Arimo", sans-serif; font-size: 13px; color: var(--navy);
  }
  .website b { font-size: 15px; }
  .contact {
    position: absolute; left: 318px; top: 70px;
    font-family: "Arimo", sans-serif; font-size: 12px; color: var(--navy); line-height: 1.35;
    white-space: nowrap;
  }
  .contact-name { font-weight: 700; font-size: 14.5px; }
  .contact-role { font-size: 12.5px; margin: 2px 0 16px 8px; }
  .contact-lines { margin-left: 14px; }
  .contact-lines .label { color: var(--sky); font-weight: 700; }
  .band-sky { position: absolute; left: 0; bottom: 0; width: 62%; height: 16px; background: var(--sky); }
  .band-navy { position: absolute; right: 0; bottom: 0; width: 37%; height: 16px; background: var(--navy); }
</style>
</head>
<body>

  <section class="card card-back" aria-label="Business card back">
    <div class="appointments">
      <h2>YOUR APPOINTMENTS</h2>
      <ol class="appointment-list">
        <li>1. <span class="slot time"></span>am/pm <span class="slot place"></span> <span class="slot date"></span>/<span class="slot date"></span>/<span class="slot date"></span></li>
        <li>2. <span class="slot time"></span>am/pm <span class="slot place"></span> <span class="slot date"></span>/<span class="slot date"></span>/<span class="slot date"></span></li>
        <li>3. <span class="slot time"></span>am/pm <span class="slot place"></span> <span class="slot date"></span>/<span class="slot date"></span>/<span class="slot date"></span></li>
        <li>4. <span class="slot time"></span>am/pm <span class="slot place"></span> <span class="slot date"></span>/<span class="slot date"></span>/<span class="slot date"></span></li>
        <li>5. <span class="slot time"></span>am/pm <span class="slot place"></span> <span class="slot date"></span>/<span class="slot date"></span>/<span class="slot date"></span></li>
        <li>6. <span class="slot time"></span>am/pm <span class="slot place"></span> <span class="slot date"></span>/<span class="slot date"></span>/<span class="slot date"></span></li>
      </ol>
    </div>
    <div class="services-panel">
      <div class="brand">
        <span class="brand-dot"></span>
        <span class="brand-name">Harvodel</span>
      </div>
      <p class="brand-sub">Psychology</p>
      <ul class="service-list">
        <li>Performance Enhancement</li>
        <li>Assessment &amp; Reports</li>
        <li>Individual &amp; Group Counselling</li>
        <li>Executive coaching &amp; Motivation</li>
        <li>Seminars &amp; Workshops</li>
      </ul>
    </div>
  </section>

  <section class="card card-front" aria-label="Business card front">
    <div class="front-brand">
      <div class="brand">
        <span class="brand-dot"></span>
        <span class="brand-name">Harvodel</span>
      </div>
      <p class="brand-sub">Psychology</p>
    </div>
    <p class="tagline">Rise To Your Finest</p>
    <p class="website">www.<b>harvodel</b>.com.au</p>

    <div class="contact">
      <p class="contact-name">Dr MARLISE QUENBY</p>
      <p class="contact-role">Director</p>
      <div class="contact-lines">
        <p>48 Wexbridge St</p>
        <p>Carranby Qld 4852</p>
        <p><span class="label">Fax:</span> 07 41 306 259</p>
        <p><span class="label">Mob:</span> 0431 562 047</p>
        <p><span class="label">Email:</span> mq@harvodel.com.au</p>
      </div>
    </div>

    <div class="band-sky"></div>
    <div class="band-navy"></div>
  </section>

</body>
</html>
```